Bright Fern Series- Face & Body Oil Label

Hi,
I need a label design for a new brand- "Bright Fern Series". Modern and expensive looking. Any color scheme. Feel free to be creative! (I'm not set on the brand name above... I was also thinking maybe "TIRA" or "PuraLume".
-Packaging: 4oz / 118mL clear glass "boston round" bottle with a white treatment pump. The product is an oil so it has a golden tint.
-Product: 4oz Biotin & Marula Face & Body Oil (note that the featured ingredients will change. Others will be "Rosehip & Vitamin E", "Lavender & Hemp Seed Oil", "Coconut Oil & Vitamin C"
-Label size: 5" x 2.5" rounded corners
-Main Highlight: "Moisturizing & Healing"
-Other Highlights:
-----non-greasy
-----all-natural
-----paraben-free
-----vegan
(feel free to use icon symbols)
-Ingredient deck attached
-Other info:
----made in Los Angeles, CA
----manufactured by Willowmere Labs LLC
----UPC
The main thing here is the logo and textures to the label. I can fill in / rearrange the info after.
Thank you,
Owen

```html
<!DOCTYPE html>
<html lang="en">
<head>
<meta charset="UTF-8">
<title>Bright Fern Series – Biotin &amp; Marula Face &amp; Body Oil Label</title>
<link href="https://fonts.googleapis.com/css2?family=Inter:wght@200;300;400&display=swap" rel="stylesheet">
<style>
  :root {
    --label-bg: #eddacb;
    --ink: #a38f7e;
    --ink-soft: #ab9886;
    --logo-ink: #9f8a76;
    --white: #ffffff;
  }
  html, body {
    margin: 0;
    padding: 0;
    width: 1200px;
    height: 627px;
    overflow: hidden;
    background: var(--label-bg);
  }
  .label {
    position: relative;
    width: 1200px;
    height: 627px;
    background: var(--label-bg);
    font-family: "Inter", Arial, sans-serif;
    color: var(--ink);
  }
  .label > * { position: absolute; margin: 0; line-height: 1; }

  .brand {
    left: 214px;
    top: 76px;
    font-size: 44px;
    font-weight: 200;
    color: var(--logo-ink);
    letter-spacing: -0.5px;
    line-height: 1.05;
    width: 260px;
  }

  .side-band {
    left: 135px;
    top: 162px;
    width: 26px;
    height: 480px;
    background: var(--white);
    border-radius: 3px 3px 0 0;
  }
  .product-type {
    left: 148px;
    top: 270px;
    transform: translate(-50%, -50%) rotate(-90deg);
    font-size: 17px;
    font-weight: 300;
    letter-spacing: 0.8px;
    white-space: nowrap;
    color: var(--ink);
  }

  .product-name {
    left: 166px;
    top: 168px;
    font-size: 104px;
    font-weight: 200;
    color: var(--white);
    letter-spacing: -3px;
    line-height: 94px;
  }

  .highlights {
    left: 163px;
    top: 376px;
    list-style: none;
    padding: 0;
    font-size: 21px;
    font-weight: 400;
    letter-spacing: 0.6px;
    color: var(--ink);
  }
  .highlights li { height: 40.3px; }

  .net-weight {
    left: 271px;
    top: 548px;
    font-size: 30px;
    font-weight: 200;
    color: var(--ink);
  }

  .ingredients {
    left: 755px;
    top: 162px;
    font-size: 19px;
    font-weight: 300;
    color: var(--ink-soft);
    letter-spacing: -0.2px;
  }
  .ingredients h2 {
    font-size: 19px;
    font-weight: 400;
    margin: 0 0 4px;
    line-height: 1;
  }
  .ingredients ul { list-style: none; margin: 0; padding: 0; }
  .ingredients li { height: 22.9px; }

  .origin {
    left: 755px;
    top: 384px;
    font-size: 19px;
    font-weight: 400;
    color: var(--ink);
  }
  .origin p { margin: 0; height: 30px; }

  .upc-area {
    left: 856px;
    top: 462px;
    width: 215px;
    height: 110px;
    background: var(--white);
    border-radius: 4px;
  }
</style>
</head>
<body>
<main class="label">
  <h1 class="brand">Bright Fern Series</h1>

  <div class="side-band"></div>
  <p class="product-type">FACE &amp; BODY OIL</p>

  <p class="product-name">biotin &amp;<br>marula</p>

  <ul class="highlights">
    <li>MOISTURIZING &amp; HEALING</li>
    <li>NON-GREASY</li>
    <li>PARABEN-FREE</li>
    <li>VEGAN</li>
  </ul>

  <p class="net-weight">4 oz</p>

  <section class="ingredients">
    <h2>Ingredients:</h2>
    <ul>
      <li>Glycine Soja (Soybean) Oil</li>
      <li>Lavandula Angustifolia (Lavender) Oil</li>
      <li>Sclerocarya Birrea (Marula) Seed Oil</li>
      <li>Cannabis Sativa (Hemp) Seed Oil</li>
      <li>Persea Gratissima (Avocado) Oil</li>
      <li>Prunus Armenica (Apricot) Kernel Oil</li>
      <li>Tocopherol</li>
      <li>Fragrance (Parfum)</li>
    </ul>
  </section>

  <div class="origin">
    <p>Made in Los Angeles, CA</p>
    <p>Manufactured by Willowmere Labs LLC</p>
  </div>

  <div class="upc-area"></div>
</main>
</body>
</html>
```